Packaging Design for Health/Beauty product

This project is for the brand new design of our new product.
Box/Tube/Images
The product is an anesthetic Skin Numbing Cream used for numbing skin for general pain relief and also before tattoos, waxing, laser hair removal and small cosmetic procedures.
Direct to end user and also to salons and studios, with view to selling in pharmacies.
This is a Brand New Product
Packaging design for the brand CALVEXO
2 components -
1. TUBE/OUTER PACKAGING design
and
2. "3D" style graphics/images suitable for marketing
******************
DELIVERABLES:
Tube:
Adobe Illustrator file (.ai) using supplied template for die lines prior to printing/manufacture and PDF files
PNG files for 3D style renderings of front, back, side, and angled left and right.
Outer Packaging:
PNG files for some 3D style renderings of front, back, side, and angled left and right.
******************
WHAT IS THE PRODUCT?
It is an anesthetic skin numbing cream, with Aloe for soothing the skin and Tea Tree
Please google “numbing cream”- images and you’ll get an idea of the 3D styling required.
But - please think “outside the box” and design something that is NOT a copy or modelled off existing brands. We want something completely new to stand out from the crowd without being too "Over The Top."
Keep the core demographic in mind.
This job had previously been given to an artist on here, but prior to completion he ceased replying to my emails. I have a #D image of what we were after.
You may either replicate what was done there (I only have a PDF image, no AI source files) OR you may go for a completely new design.
Both options will be given equal appraisal.
******************
DEMOGRAPHIC
The target market will be for pain relief for injection, vaccinations, waxing, laser hair removal - Mainly for 18-40 year olds, male/female. We also have a view to going into mainstream pharmacies as well.
We are after a visually striking design that will attract the eye and be appealing to our target market- but also a nice clean, uncluttered design.
******************
LOGO INCLUDED - Attachment
Supplied is our "Branding Logo" that is to be incorporated onto both the tube and outer packaging.
IF you have a completely different idea/color scheme that would incorporate a good logo (different than supplied) then that is also ok - it would require you to design the logo as well.
*******************
TEMPLATES - Attachment
2 Templates are supplied - 1 x Tube & 1 x Outer Package
It is for an FDA regulated drug.
The fonts/text on the templates are representative of the WORDING required.
Positioning within each panel can be altered to suit the design, this is for your guidance.
Bar code, NDC code, company logo and other required info will all be supplied.
Please also add a QR code as per the attached example form a different product
Your job is to come up with a great design.
Template provided in Adobe Illustrator (.ai) and must be delivered as same.
*********************
COLORS
Currently we have our logo in green/orange, and we think these neutral colors work well with this market.
As stated, IF you have a totally new idea for LOGO & DESIGN, feel free to use your skills!
Using extra colors comes down to your design, but keep in mind that too many colors can lose impact and not print well.
Remember this will be printed on a plastic tube and a cardboard outer packaging - so the design must be able to look good on a physical product.
Not just on a digital website.
********************
UNIQUE SELLING POINT
Our cream has both Tea Tree & Aloe in the ingredients, and if they can be highlighted in some visual way without detracting from the overall design that would be great.
Use your skills here to represent this as best you can without making it be the main focus.
********************
DRUG FACTS PANEL
Within the supplied templates is a drug facts label that will require some small text changes. WE will make those changes and forward the updated Drug Facts Panel to you.
However the existing panel DIMENSIONS within the template will not change, so you can go ahead and make your design, and we will forward the updated panel asap.
*******************
BARCODE - Attachment
Supplied is a barcode to be used as per template
Please also add a QR Code
******************
NDC CODE - a string of numbers eg/ 12345 678 90
We are still awaiting the receipt of the NDC code, and it may not arrive until after the contest is complete and the winner chosen, and the final adjustments to design made.
Please go ahead and do the main outlay. Upon receipt of the NDC I will send to you for insertion as necessary, wherein the job will be essentially finished.
Then I will need to 2D ai files and PDF templates for submission for registration, AND then also the 3D images that will have the NDC on them, exactly as the package will look once complete.
****************
3D RENDERS
I will need several HIGH QUALITY 3D images for use on our website and in marketing.
Images of the tube (different angles), the box, front and back (different angles), the tube coming out of the opened box, (different angles) - you get the idea what I need.
****************
IMPORTANT
We do not want any photos of people incorporated into the design.
We do not have a blank "3D" style tube for you to use to wrap your label around when creating the promotion style images.
I am awaiting from the manufacturer the final shaping of the tube (it will be similar to the graphic provided) BUT the cap will change shape due to new FDA Rules. Once I have that I will inform you. For now it is ok to use a simple screw cap, but please note that this will need to be changed before final sign off.
Please do your very best to create a great design.
Good luck and may the best design win!
Thankyou very much.

```html
<!DOCTYPE html>
<html lang="en">
<head>
<meta charset="utf-8">
<title>CALVEXO Carton Dieline</title>
<link href="https://fonts.googleapis.com/css2?family=Montserrat:wght@400;500;600&family=Arimo:ital,wght@0,400;0,700;1,700&display=swap" rel="stylesheet">
<style>
:root{
  --paper:#ffffff;
  --tex-a:#eef0ee;
  --tex-b:#dfe4df;
  --frame:#a9b9a6;
  --green:#5d9a3c;
  --accent:#e86a1e;
  --sage:#8aa486;
  --ink:#222;
  --rule:#b7c4b4;
}
*{box-sizing:border-box;margin:0;padding:0}
html,body{width:777px;height:1200px;overflow:hidden;background:var(--paper)}
body{position:relative;font-family:"Montserrat",sans-serif}
.area{position:absolute;background:linear-gradient(135deg,var(--tex-a) 0%,var(--tex-b) 50%,var(--tex-a) 100%)}
.panel{position:absolute;background:var(--paper);border:5px solid var(--frame)}
.logo{font-family:"Montserrat",sans-serif;font-weight:600;color:var(--green);letter-spacing:.02em;line-height:1;white-space:nowrap}
.strength{font-family:"Montserrat",sans-serif;font-size:6px;color:var(--ink);font-weight:500;white-space:nowrap}
.tagline{color:var(--sage);font-weight:500;letter-spacing:.04em;position:absolute;white-space:nowrap}
.badge{position:absolute;border-radius:50%;background:#5f7d5a;border:3px solid #dfe5de}
.claims{position:absolute;left:8px;top:36px;font-size:6.3px;line-height:8.3px;color:#9fb09c;letter-spacing:.03em}
.ndc{position:absolute;left:536px;top:71px;font-family:"Arimo",sans-serif;font-size:8px;color:#111}
.plate{position:absolute;left:654px;top:357px;transform:rotate(-90deg);transform-origin:left top;font-family:"Arimo",sans-serif;font-size:7px;font-weight:700;line-height:7px;color:#111}
.facts{position:absolute;left:166px;top:781px;width:451px;height:326px;border:5px solid var(--frame);background:var(--paper)}
.facts-inner{position:absolute;inset:0;transform:rotate(180deg);font-family:"Arimo",sans-serif;font-size:6.4px;line-height:8px;color:var(--ink);padding:3px 6px}
.facts h2{font-style:italic;font-weight:700;font-size:14px;line-height:19px;border-bottom:3px solid var(--rule)}
.facts h3{font-style:italic;font-weight:700;font-size:7.5px;line-height:9px;display:flex;justify-content:space-between}
.facts .sec{border-bottom:2px solid var(--rule);padding:2px 0}
</style>
</head>
<body>

<div class="area" role="img" aria-label="light grey swirl texture on carton board" style="left:156px;top:39px;width:474px;height:1136px;border-radius:6px"></div>
<div class="area" role="img" aria-label="light grey swirl texture on left dust flap" style="left:74px;top:236px;width:84px;height:157px;border-radius:30px 0 0 4px"></div>
<div class="area" role="img" aria-label="light grey swirl texture on left side panel" style="left:53px;top:394px;width:105px;height:205px;border-radius:4px 0 0 4px"></div>
<div class="area" role="img" aria-label="light grey swirl texture on left dust flap" style="left:74px;top:614px;width:84px;height:131px;border-radius:4px 0 0 30px"></div>
<div class="area" role="img" aria-label="light grey swirl texture on glue flap" style="left:53px;top:761px;width:105px;height:413px"></div>
<div class="area" role="img" aria-label="light grey swirl texture on right flap" style="left:628px;top:236px;width:84px;height:157px;clip-path:polygon(0 0,25% 0,40% 6%,100% 8%,100% 100%,0 100%)"></div>
<div class="area" role="img" aria-label="light grey swirl texture on right side panel" style="left:628px;top:394px;width:105px;height:205px"></div>
<div class="area" role="img" aria-label="light grey swirl texture on right flap" style="left:628px;top:614px;width:84px;height:131px;clip-path:polygon(0 0,100% 0,100% 92%,40% 94%,25% 100%,0 100%)"></div>
<div class="area" role="img" aria-label="light grey swirl texture on right glue flap" style="left:628px;top:761px;width:105px;height:413px"></div>

<div class="ndc">NDC# 00000-000-00</div>
<div class="plate">PL306028<br>V01</div>

<section class="panel" style="left:166px;top:89px;width:451px;height:135px">
  <div class="claims">SOOTHES SUNBURN<br>RELIEVES ITCH<br>STEROID FREE<br>QUICK ACTING</div>
  <div style="position:absolute;left:142px;top:40px">
    <div class="strength" style="text-align:right">4% Lidocaine Cream</div>
    <div class="logo" style="font-size:29px">CALVEXO</div>
  </div>
  <div class="tagline" style="left:0;right:0;top:104px;text-align:center;font-size:12px">PAIN RELIEVING NUMBING CREAM</div>
  <div class="badge" style="left:392px;top:38px;width:48px;height:48px"></div>
</section>

<section class="panel" style="left:166px;top:247px;width:451px;height:135px">
  <div style="position:absolute;left:24px;top:22px">
    <div class="strength" style="text-align:right;font-size:4.5px">4% Lidocaine Cream</div>
    <div class="logo" style="font-size:17px">CALVEXO</div>
  </div>
  <div class="tagline" style="left:146px;top:30px;font-size:7px">PAIN RELIEVING NUMBING CREAM</div>
  <div class="badge" style="left:391px;top:10px;width:48px;height:48px"></div>
  <div class="tagline" style="left:0;right:0;top:62px;text-align:center;font-size:12.5px;line-height:16px;letter-spacing:.08em">WORKS FAST FOR RAPID RELIEF<br>MADE WITH ALOE &amp; TEA TREE<br>NUMBS THE SKIN~SAFE &amp; SOOTHING</div>
</section>

<section style="position:absolute;left:74px;top:418px;width:72px;height:158px;background:var(--paper)">
  <div style="position:absolute;left:70px;top:20px;transform:rotate(90deg);transform-origin:left top">
    <div class="logo" style="font-size:21px">CALVEXO</div>
    <div class="strength" style="font-size:5px">4% Lidocaine Cream</div>
  </div>
  <div class="tagline" style="left:30px;top:20px;transform:rotate(90deg);transform-origin:left top;font-size:5.8px;color:#8a9886">PAIN RELIEVING NUMBING CREAM</div>
</section>

<section class="panel" style="left:166px;top:405px;width:451px;height:188px">
  <div style="position:absolute;left:42px;top:62px">
    <div class="strength" style="text-align:right;font-size:9px">4% Lidocaine Cream</div>
    <div class="logo" style="font-size:44px">CALVEXO</div>
  </div>
  <div class="tagline" style="left:44px;top:155px;font-size:13px">PAIN RELIEVING NUMBING CREAM</div>
  <div class="badge" style="left:342px;top:58px;width:74px;height:74px"></div>
  <div class="tagline" style="left:329px;top:160px;font-size:7.5px;color:#93a18f">NET WT. 2.0 OZ. (56.7G)</div>
</section>

<section class="panel" style="left:166px;top:609px;width:451px;height:134px">
  <div style="position:absolute;left:62px;top:44px">
    <div class="strength" style="text-align:right">4% Lidocaine Cream</div>
    <div class="logo" style="font-size:32px">CALVEXO</div>
  </div>
  <div class="tagline" style="left:64px;top:108px;font-size:9px">PAIN RELIEVING NUMBING CREAM</div>
</section>

<section class="facts">
  <div class="facts-inner">
    <h2>Drug Facts</h2>
    <div class="sec"><h3><span>Active ingredient</span><span>Purpose</span></h3>
      <p style="display:flex;justify-content:space-between"><span>Lidocaine 4%</span><span>Topical analgesic</span></p></div>
    <div class="sec"><h3>Use</h3><p>for the temporary relief of pain associated with:</p>
      <p>■ minor burns ■ sunburns ■ minor cuts ■ scrapes ■ insect bites ■ minor skin irritations</p></div>
    <div class="sec"><h3>Warnings</h3><p><b>For external use only.</b></p>
      <p><b>Do not use</b></p>
      <p>■ on large areas of the body ■ on broken, blistered, or oozing skin ■ on deep or puncture wounds</p>
      <p>■ for more than one week without consulting a doctor ■ if seal on tube is punctured or missing</p>
      <p><b>When using this product,</b> avoid contact with eyes.</p>
      <p><b>Stop use and ask a doctor if</b></p>
      <p>■ condition worsens ■ symptoms persist for more than 7 days ■ condition clears up and occurs again within a few days</p>
      <p><b>If pregnant or breast-feeding,</b> ask a health professional before use.</p></div>
    <div class="sec"><p><b>Keep out of reach of children.</b> If swallowed, get medical help, or contact a Poison Control Center right away. 555-018-4400.</p></div>
    <div class="sec"><h3>Directions</h3>
      <p><b>Adults and children 2 years old and older</b></p>
      <p>■ clean the affected area</p>
      <p>■ apply a thin layer of product to affected area every 6 to 8 hours up to 3 times every 24 hours</p>
      <p><b>Children under 2 years old</b></p><p>Consult a doctor</p></div>
    <div class="sec"><h3>Other information</h3>
      <p>■ store at 15 to 30°C (59 to 86°F) ■ close cap tightly after use</p></div>
    <div class="sec"><h3>Inactive ingredients</h3>
      <p>aloe barbadensis leaf juice, arginine, benzophenone-4, cetyl alcohol, dimethyl sulfoxide, melaleuca alternifolia (tea tree) leaf oil, phenoxyethanol (and) caprylyl glycol (and) potassium sorbate (and) water (and) hexylene glycol, purified water, simmondsia chinensis (jojoba) seed oil, sodium polyacrylate, stearic acid</p></div>
    <div style="padding-top:2px"><h3 style="display:block">Questions or Comments? <span style="font-style:normal;font-weight:400;font-size:6.5px">555-014-2290 or www.calvexolabs.example</span></h3></div>
  </div>
</section>

<div style="position:absolute;left:498px;top:1123px;width:97px;height:43px;background:var(--paper);display:flex;align-items:center;justify-content:center">
  <div class="logo" style="font-size:13px;transform:rotate(180deg)">CALVEXO</div>
</div>

</body>
</html>
```